Brook Forge - Crypto Currency Miner Powered by Renewable Energy Website

We Need Web Pages Design for Website for Crypto Currency Miner

Serivices include:
Mining Rig Sales
Housing for Rigs turnkey on renewable energy grid
Cloud Mining term packages
Updates

http://www.vaultrigratings.example (Competitors sites)

Target Market(s)

Investers for Mining Rigs and terms for 1,2 or 3 years of Hash rate

Industry/Entity Type

Mining

Number of Pages Required

5+ page

Font styles to use
Sans Serif

Colors
add136
9bcb3c
606060
474747
ffc214
cadf82
fbee3e
876aae
6b449b

Requirements
Must have
• Pictures of Solar, Wind and power Factor Correction units
Nice to have
• e-commerce platform so contract terms can be purchased through website
Should not have
• Heavy construction equipment

```html
<!DOCTYPE html>
<html lang="en">
<head>
<meta charset="utf-8">
<title>Brook Forge – Renewable Crypto Mining</title>
<link rel="stylesheet" href="https://fonts.googleapis.com/css2?family=Oswald:wght@400;500&family=Roboto+Condensed:wght@400;700&display=swap">
<style>
:root{
  --green:#3db54a;
  --green-light:#9bcb3c;
  --yellow:#ffc214;
  --yellow-soft:#fbee3e;
  --gray:#606060;
  --gray-dark:#474747;
  --backdrop:#c4c4c4;
  --white:#ffffff;
  --tablet-frame:#1b1b1b;
}
*{margin:0;padding:0;box-sizing:border-box}
html,body{width:1200px;height:1200px;overflow:hidden;background:var(--backdrop)}
body{position:relative;font-family:"Roboto Condensed",sans-serif}
.page{position:absolute;left:450px;top:28px;width:300px;height:1144px;background:var(--white);overflow:hidden;box-shadow:6px 8px 18px rgba(0,0,0,.35)}
.abs{position:absolute}
.heading{font-family:"Oswald",sans-serif;font-weight:400;line-height:1.05}
.copy{font-size:3.2px;line-height:1.45}
.btn{position:absolute;font-family:"Oswald",sans-serif;font-size:4.5px;padding:1.5px 6px;letter-spacing:.2px}
.btn--fill{background:var(--green);color:var(--white)}
.btn--line{border:.6px solid var(--white);color:var(--white)}
.brand{display:flex;align-items:center;gap:3px;color:var(--white);font-family:"Roboto Condensed",sans-serif;font-size:7px}
.brand__dot{width:8px;height:8px;border-radius:50%;background:var(--white)}
.marker{display:inline-block;width:5px;height:5px;margin-right:4px;vertical-align:middle}

/* hero */
.hero{left:0;top:0;width:300px;height:192px;background:radial-gradient(circle at 60% 35%,#b8901c,#5a4608 55%,#1f1a06)}
.nav{left:38px;top:8px;width:262px;display:flex;align-items:center}
.nav__links{display:flex;gap:9px;margin-left:20px;font-size:3.4px;color:var(--white)}
.hero__coin{left:179px;top:126px;width:80px;height:80px;border-radius:50%;background:radial-gradient(circle at 40% 35%,#ffe38a,#d9a52a 60%,#8a6512);z-index:2;box-shadow:0 6px 10px rgba(0,0,0,.3)}
.hero__title{left:33px;top:118px;color:var(--white);font-size:15.5px;text-transform:uppercase}

/* features */
.features{left:0;top:192px;width:300px;height:140px}
.feature{position:absolute;top:24px;width:70px;text-align:center;color:#5a4a10}
.feature svg{display:block;margin:0 auto 8px}
.feature__title{font-family:"Oswald",sans-serif;font-size:5px;line-height:1.25;text-transform:uppercase;margin-bottom:8px}
.feature .copy{font-size:2.8px}

/* buy */
.buy__title{left:40px;top:350px;color:var(--green);font-size:13px}
.tablet{left:140px;top:294px;z-index:3}

/* why */
.why{left:0;top:482px;width:300px;height:174px;background:var(--gray-dark)}
.step{position:absolute;width:18px;height:18px;border-radius:50%;border:2px solid;background:var(--white);font-family:"Oswald",sans-serif;font-size:7px;text-align:center;line-height:14px}
.step__label{position:absolute;font-size:3.4px;font-weight:700}
.why__title{left:174px;top:36px;color:var(--white);font-size:12px;text-transform:uppercase}

/* about */
.about{left:0;top:656px;width:300px;height:182px;background:linear-gradient(160deg,#8a6a4c,#c98a3c 40%,#4c5a3a 75%,#2e3a2a)}
.about__title{left:40px;top:98px;color:var(--white);font-size:13px}

/* consult */
.consult{left:0;top:838px;width:300px;height:176px;background:var(--green);overflow:hidden}
.consult__coin{left:-34px;top:0;width:176px;height:176px;border-radius:50%;background:radial-gradient(circle at 55% 40%,#ffe9a0,#e0b440 55%,#a07818)}
.consult__title{left:134px;top:52px;color:var(--white);font-size:10px;text-transform:uppercase}

/* footer */
.footer{left:0;top:1017px;width:300px;height:105px;background:var(--gray-dark);color:var(--white)}
.footer__head{font-family:"Oswald",sans-serif;font-size:6px;margin-bottom:3px}
.footer__list{font-size:3px;line-height:1.7;list-style:none}
.post{display:flex;gap:3px;margin-bottom:6px;font-size:3px;line-height:1.45}
.post__thumb{width:16px;height:16px;background:var(--yellow);flex:none}
.bar{left:0;top:1122px;width:300px;height:22px;background:#e9e9e9}
.bar__copy{font-size:2.6px;color:#555}
.social{display:flex;gap:2px}
.social span{width:4px;height:4px;border-radius:50%;background:#2a6fb5}
</style>
</head>
<body>
<main class="page">

  <section class="hero abs" role="img" aria-label="Gold-toned photo of a phone with a rising chart and coins resting on a circuit board"></section>
  <nav class="nav abs">
    <div class="brand"><span class="brand__dot"></span>Brook Forge</div>
    <div class="nav__links"><span>HOME</span><span>PRICING</span><span>OUR OFFER</span><span>ABOUT US</span><span>CUSTOMER SERVICE</span></div>
  </nav>
  <h1 class="hero__title heading abs">Start<br>Brook Forge<br>Today!</h1>

  <section class="features abs">
    <svg class="abs" style="left:0;top:0" width="300" height="140" viewBox="0 0 300 140">
      <polygon points="0,0 300,0 300,134 0,100" fill="var(--yellow)"/>
    </svg>
    <div class="feature" style="left:40px">
      <svg width="18" height="18" viewBox="0 0 18 18" fill="none" stroke="#7a6220" stroke-width=".8"><circle cx="9" cy="9" r="1.6"/><path d="M9 7.4V1.5M10.4 9.8l5 3M7.6 9.8l-5 3"/></svg>
      <div class="feature__title">Wind Power<br>Investment</div>
      <p class="copy">Don't wrestle with rig assembly and hot, noisy miners at home. We have the fastest mining hardware running for you already!</p>
    </div>
    <div class="feature" style="left:115px">
      <svg width="18" height="18" viewBox="0 0 18 18" fill="none" stroke="#7a6220" stroke-width=".8"><rect x="3" y="3" width="12" height="8"/><path d="M3 7h12M7 3v8M11 3v8M9 11v5M6 16h6"/></svg>
      <div class="feature__title">Solar Power<br>Investment</div>
      <p class="copy">Don't wrestle with rig assembly and hot, noisy miners at home. We have the fastest mining hardware running for you already!</p>
    </div>
    <div class="feature" style="left:190px">
      <svg width="18" height="18" viewBox="0 0 18 18" fill="none" stroke="#7a6220" stroke-width=".8"><rect x="2" y="6" width="14" height="10" rx="1"/><path d="M4 6l8-4 2 4M12 10h4v3h-4z"/></svg>
      <div class="feature__title">Get Your First<br>Payout Today</div>
      <p class="copy">Don't wrestle with rig assembly and hot, noisy miners at home. We have the fastest mining hardware running for you already!</p>
    </div>
  </section>
  <div class="hero__coin abs" role="img" aria-label="Gold crypto coin"></div>

  <h2 class="buy__title heading abs"><span class="marker" style="background:var(--green)"></span>Buy And Sell Bitcoin</h2>
  <div class="abs" style="left:50px;top:370px;width:100px;color:var(--green)">
    <p class="copy" style="font-size:3.6px">Lorem ipsum dolor sit amet, consectetur adipiscing elit. At quam praesentium, distinctio dicta molestias dignissimos.</p>
    <p class="copy" style="color:#777;margin-top:4px">Lorem ipsum dolor sit amet, consectetur adipiscing elit. Quam earum, provident sit, porro quaerat dolores blanditiis, sint pariatur nisi aliquid consequatur officiis. Eaque iure, nostrum? Ut incidunt mollitia quidem.</p>
  </div>
  <span class="btn btn--fill" style="left:116px;top:408px">JOIN US</span>

  <section class="why abs">
    <svg class="abs" style="left:0;top:0" width="300" height="174" viewBox="0 0 300 174" fill="none" stroke-width=".6">
      <path d="M119 31H163" stroke="#1e8fd0"/>
      <path d="M40 63H92" stroke="#1aa3a0"/>
      <path d="M119 94H163" stroke="var(--yellow)"/>
      <path d="M40 127H92" stroke="var(--green-light)"/>
    </svg>
    <div class="step" style="left:85px;top:39px;border-color:#1e8fd0;color:#1e8fd0">A</div>
    <div class="step" style="left:101px;top:70px;border-color:#1aa3a0;color:#1aa3a0">B</div>
    <div class="step" style="left:86px;top:102px;border-color:var(--yellow);color:#c99400">C</div>
    <div class="step" style="left:101px;top:133px;border-color:var(--green-light);color:#5f9a1a">D</div>
    <span class="step__label" style="left:119px;top:36px;color:#1e8fd0">Safe And Secure</span>
    <span class="step__label" style="left:58px;top:68px;color:#1aa3a0">Mobile App</span>
    <span class="step__label" style="left:119px;top:99px;color:var(--yellow)">Secure Wallet</span>
    <span class="step__label" style="left:40px;top:131px;color:var(--green-light)">Covered By Insurance</span>
    <h2 class="why__title heading abs">Why Choose<br>Brook Forge?</h2>
    <div class="abs" style="left:174px;top:64px;width:80px;color:var(--white)">
      <p class="copy">Northwind Hashing offers you a smart and easy way to invest your money. Our mining system is suitable for those who are new to the world of crypto currencies, as well as for experienced investors. It is a large scale multi-algorithm cloud mining service offering an alternative for those who would like to engage in mining.</p>
      <p class="copy" style="margin-top:4px">We are a team of experts in the digital currency sector, and our mining algorithm is designed to provide the most efficient and reliable mining rentals.</p>
    </div>
    <span class="btn btn--line" style="left:220px;top:146px">MORE...</span>
  </section>

  <svg class="tablet abs" width="160" height="220" viewBox="0 0 160 220" role="img" aria-label="Tablet showing the Brook Forge home screen on a yellow to green gradient">
    <defs>
      <linearGradient id="screenFill" x1="0" y1="0" x2="0" y2="1">
        <stop offset="0" stop-color="var(--yellow)"/>
        <stop offset="1" stop-color="var(--green)"/>
      </linearGradient>
    </defs>
    <polygon points="50,2 162,30 134,218 2,184" fill="var(--tablet-frame)" stroke="var(--tablet-frame)" stroke-width="6" stroke-linejoin="round"/>
    <polygon points="56,12 160,38 128,204 12,176" fill="url(#screenFill)"/>
  </svg>

  <section class="about abs" role="img" aria-label="Photo of a wind turbine over fields at sunset"></section>
  <h2 class="about__title heading abs" style="top:756px"><span class="marker" style="background:var(--white)"></span>About Brook Forge</h2>
  <div class="abs" style="left:50px;top:780px;width:100px;color:var(--white)">
    <p class="copy" style="font-size:3.6px">Lorem ipsum dolor sit amet, consectetur adipiscing elit. At quam praesentium, distinctio dicta molestias dignissimos.</p>
    <p class="copy" style="margin-top:4px">Lorem ipsum dolor sit amet, consectetur adipiscing elit. Quam earum, provident sit, porro quaerat dolores blanditiis, sint pariatur nisi aliquid. Eaque iure, nostrum? Ut incidunt mollitia quidem.</p>
  </div>
  <span class="btn btn--fill" style="left:116px;top:819px">JOIN US</span>

  <section class="consult abs">
    <div class="consult__coin abs" role="img" aria-label="Large gold digital currency coin"></div>
    <h2 class="consult__title heading abs"><span class="marker" style="background:var(--white)"></span>Are You Looking For<br>&nbsp;&nbsp;&nbsp;A Consalting?</h2>
    <div class="abs" style="left:144px;top:80px;width:100px;color:var(--white)">
      <p class="copy" style="font-size:3.6px">Lorem ipsum dolor sit amet, consectetur adipiscing elit. At quam praesentium, distinctio dicta molestias dignissimos.</p>
      <p class="copy" style="margin-top:4px">Lorem ipsum dolor sit amet, consectetur adipiscing elit. Quam earum, provident sit, porro quaerat dolores blanditiis. Eaque iure, nostrum? Ut incidunt mollitia quidem.</p>
    </div>
    <span class="btn btn--fill" style="left:210px;top:119px;background:#5fcf6a">MORE...</span>
  </section>

  <footer class="footer abs">
    <div class="abs" style="left:38px;top:12px;width:60px">
      <div class="brand" style="margin-bottom:6px"><span class="brand__dot"></span>Brook Forge</div>
      <p class="copy" style="font-size:3px">Lorem ipsum dolor sit amet consectetur adipiscing elit sed do eiusmod tempor incididunt ut labore et dolore magna aliqua ut enim ad minim veniam quis nostrud exercitation.</p>
    </div>
    <div class="abs" style="left:120px;top:12px">
      <div class="footer__head">Links</div>
      <ul class="footer__list"><li>Home</li><li>About Us</li><li>Services</li><li>Our Offer</li><li>Contact Us</li></ul>
    </div>
    <div class="abs" style="left:154px;top:12px;width:60px">
      <div class="footer__head">Location</div>
      <p class="copy" style="font-size:3px">Excepteur sint occaecat cupidat non proident sunt.<br>48 Quarry Lane, Millbrook.</p>
      <p class="copy" style="font-size:3px;margin-top:6px">(00) 000 111 222</p>
      <p class="copy" style="font-size:3px;margin-top:6px">(00) 000 111 222</p>
      <p class="copy" style="font-size:3px;margin-top:6px">info@brookforge.example</p>
    </div>
    <div class="abs" style="left:224px;top:12px;width:66px">
      <div class="footer__head">Popular Post</div>
      <div class="post"><span class="post__thumb"></span><span>11 Things You Need to Know About Mining – Rare Facts<br>Jun 14, 2018</span></div>
      <div class="post"><span class="post__thumb"></span><span>11 Things You Need to Know About Mining – Rare Facts<br>Jun 14, 2018</span></div>
    </div>
  </footer>

  <div class="bar abs">
    <div class="social abs" style="left:230px;top:8px"><span></span><span></span><span></span></div>
    <span class="bar__copy abs" style="left:46px;top:16px">© Copyright 2018 Brook Forge All Rights Reserved</span>
    <span class="bar__copy abs" style="left:204px;top:16px">Privacy Policy | Partners | Sitemap</span>
  </div>

</main>
</body>
</html>
```